HairDressing and Beauty Salon Website

**Any private solicitations sent outside this platform will be ignored**

I need a website design for my luxury hair dressing and beauty salon.

The style to follow for this website can should match the following designs;
www.qerntavo.com.au
www.dumisker.com.au

The design should incorporate a prominent "Book Appointment" button.

The design should incorporate a "Buy Gift Certificate" button.

The main page should provide a reviews section where I can display customer reviews.

Colors
Main colors are white and black with purple / teal color highlights.

I need 5 pages designed;
About -> See archive with about text. Should have a top header image as shown in the websites above
Services -> List various services offered included in the Services folder of the attached archive
Shopping -> A grid of hair style related products for sale
Photos -> Photos are provided in the Photos folder in the attached archive
Contact -> Include a google map, address, book appointment button

Target Market(s)

High end luxury beauty and hair salon

Industry/Entity Type

Hair And Beauty

Number of Pages Required

5+ page

Colors
876aae
86cfc6
ffffff

Requirements
Must have
• - Book appointment button
- Social media buttons + Orchard Appshelf + Brindle App Market buttons to download mobile app associated with website

```html
<!DOCTYPE html>
<html lang="en">
<head>
<meta charset="utf-8">
<title>Mirelle Sorvane — Hair &amp; Beauty Salon</title>
<link href="https://fonts.googleapis.com/css2?family=Arimo:wght@400;700&family=Cormorant+SC:wght@500;600&display=swap" rel="stylesheet">
<style>
:root{
  --purple:#876aae;
  --teal:#86cfc6;
  --white:#ffffff;
  --black:#000000;
  --ink:#333333;
  --muted:#777777;
  --grey-bg:#f4f4f4;
  --footer:#3a3a3a;
  --gold:#f5c518;
}
*{margin:0;padding:0;box-sizing:border-box}
html,body{width:1200px;height:4260px;overflow:hidden}
body{font-family:'Arimo',Arial,sans-serif;color:var(--ink);background:var(--white);position:relative}
.serif{font-family:'Cormorant SC',Georgia,serif;font-weight:500}
section,header,footer{position:absolute;left:0;width:1200px}
.btn{position:absolute;display:flex;align-items:center;justify-content:center;gap:10px;background:var(--purple);color:var(--white);font-weight:700;font-size:13px;text-transform:uppercase;border-radius:3px;letter-spacing:.2px}
.btn .arrow{width:14px;height:14px}
.btn.teal{background:var(--teal)}
.rule{position:absolute;height:2px;width:40px;background:var(--teal)}

/* header */
.site-header{top:0;height:85px;background:var(--black)}
.brand{position:absolute;left:113px;top:12px;color:var(--white);text-align:left}
.brand .mark{font-family:'Cormorant SC',Georgia,serif;font-size:26px;line-height:30px;letter-spacing:.5px}
.brand .by{font-size:10px;letter-spacing:1px;margin-top:4px;text-transform:uppercase}
.main-nav{position:absolute;left:324px;top:34px;display:flex;gap:29px;font-size:14px;font-weight:700;color:var(--white)}
.main-nav .active{color:var(--teal)}
.site-header .btn{left:879px;top:20px;width:204px;height:46px}

/* hero */
.hero{top:85px;height:560px}
.hero .photo{position:absolute;inset:0;background:linear-gradient(90deg,#1e1e1e 0%,#4a4a4a 45%,#8a8a8a 75%,#5a5a5a 100%)}
.hero h1{position:absolute;left:113px;top:130px;font-size:64px;color:var(--white);font-weight:500;letter-spacing:1px}
.hero p{position:absolute;left:113px;top:216px;width:500px;font-size:14px;line-height:24px;color:var(--white)}
.hero .btn{left:113px;top:288px;width:152px;height:48px}
.app-badge{position:absolute;top:370px;height:46px;background:#000;border:1px solid #888;border-radius:7px;color:var(--white);display:flex;flex-direction:column;justify-content:center;padding-left:14px}
.app-badge small{font-size:9px;text-transform:uppercase}
.app-badge span{font-size:15px;font-weight:700}
.play{position:absolute;left:998px;top:238px}

/* about */
.about{top:645px;height:545px}
.about .photo{position:absolute;left:118px;top:96px;width:433px;height:351px;background:var(--white);box-shadow:0 2px 10px rgba(0,0,0,.2);padding:6px}
.about .photo div{width:100%;height:100%;background:linear-gradient(120deg,#c9c9c9,#6d6d6d 55%,#2a2a2a)}
.about h2{position:absolute;left:618px;top:96px;font-size:42px;color:#222}
.about .rule{left:618px;top:153px}
.about p{position:absolute;left:618px;top:175px;width:470px;font-size:13.5px;line-height:27.5px;color:var(--muted)}
.about .btn{left:618px;top:387px;width:152px;height:48px}

/* services */
.services{top:1190px;height:728px;background:var(--grey-bg)}
.services h2{position:absolute;left:112px;top:54px;font-size:42px;color:#222}
.services .rule{left:112px;top:112px}
.services .btn{left:884px;top:62px;width:203px;height:48px}
.service{position:absolute;width:318px;height:253px;color:var(--white);font-weight:700;font-size:15px;display:flex;align-items:flex-end;justify-content:center;padding-bottom:40px}
.service.s1{background:linear-gradient(160deg,#b9a08a,#5a4537)}
.service.s2{background:linear-gradient(160deg,#d9c0a3,#7a4d3a)}
.service.s3{background:linear-gradient(160deg,#b8aea6,#4e3e35)}
.service.s4{background:linear-gradient(160deg,#c2a178,#473528)}
.service.s5{background:linear-gradient(160deg,#f0f0f0,#3a3a3a)}
.service.s6{background:linear-gradient(160deg,#a9a5a2,#363331)}

/* vouchers */
.vouchers{top:1987px;height:316px}
.vouchers .photo{position:absolute;inset:0;background:linear-gradient(90deg,#a78db5,#c9b3d1 50%,#b49ac2)}
.vouchers h2{position:absolute;left:0;width:100%;padding-left:360px;top:48px;text-align:center;font-size:40px;color:var(--white)}
.vouchers .rule{left:770px;top:103px;background:var(--white)}
.vouchers p{position:absolute;left:470px;width:640px;top:136px;text-align:center;font-size:14.5px;line-height:24px;color:var(--white)}
.vouchers .btn{left:686px;top:206px;width:205px;height:48px}

/* testimonials */
.testimonials{top:2303px;height:500px}
.testimonials h2{position:absolute;left:0;width:100%;top:78px;text-align:center;font-size:42px;color:#222}
.testimonials .rule{left:580px;top:136px}
.card{position:absolute;top:188px;width:316px;height:230px;background:var(--white);box-shadow:0 0 8px rgba(0,0,0,.12);padding:30px 24px}
.card.featured{background:var(--purple);color:var(--white)}
.card .quote{width:30px;height:24px;display:block}
.card p{margin-top:20px;font-size:13px;line-height:23px;font-style:italic;color:var(--muted)}
.card.featured p{color:var(--white)}
.card .stars{margin-top:8px;color:var(--gold);font-size:16px;letter-spacing:2px}
.card.featured .stars{color:var(--white)}
.card .who{margin-top:10px;font-size:13px;color:var(--muted)}
.card .who b{color:#222}
.card.featured .who,.card.featured .who b{color:var(--white)}

/* gallery */
.gallery{top:2803px;height:640px}
.gallery h2{position:absolute;left:0;width:100%;top:0;text-align:center;font-size:42px;color:#222}
.gallery .rule{left:580px;top:58px}
.tile{position:absolute;width:233px;height:205px;background:linear-gradient(150deg,#f2f2f2,#d6d6d8 60%,#bdbcc2)}
.tile.alt{background:linear-gradient(150deg,#e4def2,#c7bde0 60%,#a99cc8)}
.tile.dark{background:linear-gradient(150deg,#e8e8e8,#9aa3a8 60%,#3c4348)}

/* contact */
.contact{top:3443px;height:516px}
.contact .panel{position:absolute;left:0;top:0;width:600px;height:516px;background:var(--purple)}
.contact h2{position:absolute;left:145px;top:48px;font-size:42px;color:var(--white)}
.contact .rule{left:147px;top:104px;background:var(--white)}
.info{position:absolute;left:147px;display:flex;align-items:center;gap:22px;color:var(--white);font-size:14px;font-weight:700;line-height:20px}
.info .ico{width:46px;height:46px;border-radius:50%;background:var(--white);display:flex;align-items:center;justify-content:center;flex:none}
.contact .btn{left:147px;top:412px;width:203px;height:45px}
.contact .map{position:absolute;left:600px;top:0;width:600px;height:516px;background:linear-gradient(135deg,#eae6dc,#f3f1ea 50%,#e0e7d8)}

/* footer */
.site-footer{top:3959px;height:301px;background:var(--footer);color:var(--white);text-align:center}
.site-footer .brand{position:static;text-align:center;padding-top:70px}
.footer-nav{display:flex;justify-content:center;gap:30px;margin-top:38px;font-size:13px;font-weight:700}
.site-footer small{display:block;margin-top:30px;font-size:13px}
</style>
</head>
<body>

<header class="site-header">
  <div class="brand"><div class="mark">Maison Velour</div><div class="by">by MirelleSorvane</div></div>
  <nav class="main-nav"><span class="active">Home</span><span>About Us</span><span>Our Services</span><span>Shopping</span><span>Gallery</span><span>Contact Us</span></nav>
  <a class="btn">Book an Appointment
    <svg class="arrow" viewBox="0 0 14 14"><rect x="1" y="2" width="12" height="11" rx="1" fill="none" stroke="#fff" stroke-width="1.5"/><line x1="1" y1="5.5" x2="13" y2="5.5" stroke="#fff" stroke-width="1.5"/><line x1="4" y1="0.5" x2="4" y2="3" stroke="#fff" stroke-width="1.5"/><line x1="10" y1="0.5" x2="10" y2="3" stroke="#fff" stroke-width="1.5"/></svg>
  </a>
</header>

<section class="hero">
  <div class="photo" role="img" aria-label="Black and white photo of a barber styling a bearded client's hair"></div>
  <h1 class="serif">Mirelle Sorvane</h1>
  <p>Lorem ipsum dolor sit amet, consectetur adipiscing elit, sed do eiusmod tempor incididunt ut labore et dolore magna aliqua.</p>
  <a class="btn">Get Started <svg class="arrow" viewBox="0 0 14 14"><circle cx="7" cy="7" r="6.5" fill="#fff"/><path d="M5.5 4l3 3-3 3" fill="none" stroke="#876aae" stroke-width="1.8"/></svg></a>
  <div class="app-badge" style="left:113px;width:142px"><small>Get it on</small><span>Brindle App Market</span></div>
  <div class="app-badge" style="left:267px;width:142px"><small>Download on</small><span>Orchard Appshelf</span></div>
  <svg class="play" width="80" height="80" viewBox="0 0 80 80"><circle cx="40" cy="40" r="39" fill="#fff" opacity=".85"/><circle cx="40" cy="40" r="28" fill="#fff"/><circle cx="40" cy="40" r="20" fill="#876aae"/><path d="M35 31l13 9-13 9z" fill="#fff"/></svg>
</section>

<section class="about">
  <div class="photo"><div role="img" aria-label="Photo of a stylist cutting a client's hair in the salon"></div></div>
  <h2 class="serif">About Us</h2>
  <div class="rule"></div>
  <p>MirelleSorvane is a boutique hair and beauty salon operating in the lovely harbourside suburb of Coral Bay. The salon is a family business that prides itself on its close team of hair and beauty professionals that provide a fantastic environment for its clients and friends to enjoy an amazing lux experience. MirelleSorvane is the Flagship Institut for Maison Velour in Australia and operates from its new state of the art facilities providing the perfect destination for all things luxury</p>
  <a class="btn">Learn More <svg class="arrow" viewBox="0 0 14 14"><circle cx="7" cy="7" r="6.5" fill="#fff"/><path d="M5.5 4l3 3-3 3" fill="none" stroke="#876aae" stroke-width="1.8"/></svg></a>
</section>

<section class="services">
  <h2 class="serif">Our Services</h2>
  <div class="rule"></div>
  <a class="btn">View All Services <svg class="arrow" viewBox="0 0 14 14"><circle cx="7" cy="7" r="6.5" fill="#fff"/><path d="M5.5 4l3 3-3 3" fill="none" stroke="#876aae" stroke-width="1.8"/></svg></a>
  <div class="service s1" role="img" aria-label="Blow dry photo" style="left:112px;top:160px">BLOWDRY</div>
  <div class="service s2" role="img" aria-label="Braided hairstyle photo" style="left:442px;top:160px">BRAIDING</div>
  <div class="service s3" role="img" aria-label="Hair care photo" style="left:772px;top:160px">HAIR CARE RITUALS</div>
  <div class="service s4" role="img" aria-label="Hair extension photo" style="left:112px;top:435px">HAIR EXTENSION</div>
  <div class="service s5" role="img" aria-label="Sleek straight hair photo" style="left:442px;top:435px">FORM &amp; SMOOTH</div>
  <div class="service s6" role="img" aria-label="Haircut photo" style="left:772px;top:435px">CUTIING</div>
</section>

<section class="vouchers">
  <div class="photo" role="img" aria-label="Lilac-toned beauty portrait background"></div>
  <h2 class="serif">Mirelle Sorvane Gift Vouchers</h2>
  <div class="rule"></div>
  <p>Lorem ipsum dolor sit amet, consectetur adipiscing elit, sed do eiusmod tempor incididunt ut labore et dolore magna aliqua. Ut enim ad minim veniam, quis nostrud</p>
  <a class="btn teal">Buy Gift Certificate <svg class="arrow" viewBox="0 0 14 14"><circle cx="7" cy="7" r="6.5" fill="#fff"/><path d="M5.5 4l3 3-3 3" fill="none" stroke="#86cfc6" stroke-width="1.8"/></svg></a>
</section>

<section class="testimonials">
  <h2 class="serif">What Our Clients Say</h2>
  <div class="rule"></div>
  <div class="card" style="left:102px">
    <svg class="quote" viewBox="0 0 30 24"><path d="M0 24V12Q0 2 12 0v5Q6 6 6 11h6v13zM18 24V12q0-10 12-12v5q-6 1-6 6h6v13z" fill="#876aae"/></svg>
    <p>Sed ut perspiciatis unde omnis iste natus error sit voluptatem accusantidoloremque laudantium, totam rem aperiam</p>
    <div class="stars">★★★★★</div>
    <div class="who"><b>JOHN DOE ,</b> Businessman</div>
  </div>
  <div class="card featured" style="left:441px">
    <svg class="quote" viewBox="0 0 30 24"><path d="M0 24V12Q0 2 12 0v5Q6 6 6 11h6v13zM18 24V12q0-10 12-12v5q-6 1-6 6h6v13z" fill="#fff"/></svg>
    <p>Sed ut perspiciatis unde omnis iste natus error sit voluptatem accusantidoloremque laudantium, totam rem aperiam</p>
    <div class="stars">★★★★★</div>
    <div class="who"><b>JOHN DOE ,</b> Businessman</div>
  </div>
  <div class="card" style="left:780px">
    <svg class="quote" viewBox="0 0 30 24"><path d="M0 24V12Q0 2 12 0v5Q6 6 6 11h6v13zM18 24V12q0-10 12-12v5q-6 1-6 6h6v13z" fill="#876aae"/></svg>
    <p>Sed ut perspiciatis unde omnis iste natus error sit voluptatem accusantidoloremque laudantium, totam rem aperiam</p>
    <div class="stars">★★★★★</div>
    <div class="who"><b>JOHN DOE ,</b> Businessman</div>
  </div>
</section>

<section class="gallery">
  <h2 class="serif">Our Gallery</h2>
  <div class="rule"></div>
  <div class="tile dark" role="img" aria-label="Salon interior photo" style="left:0;top:111px"></div>
  <div class="tile" role="img" aria-label="Salon styling stations photo" style="left:241px;top:111px"></div>
  <div class="tile" role="img" aria-label="Salon interior photo" style="left:483px;top:111px"></div>
  <div class="tile alt" role="img" aria-label="Salon stations photo" style="left:724px;top:111px"></div>
  <div class="tile" role="img" aria-label="Salon glass room photo" style="left:967px;top:111px"></div>
  <div class="tile" role="img" aria-label="Salon mirrors photo" style="left:0;top:323px"></div>
  <div class="tile alt" role="img" aria-label="Wash basins photo" style="left:241px;top:323px"></div>
  <div class="tile alt" role="img" aria-label="Wash area photo" style="left:483px;top:323px"></div>
  <div class="tile dark" role="img" aria-label="Product display photo" style="left:724px;top:323px"></div>
  <div class="tile dark" role="img" aria-label="Salon reception photo" style="left:967px;top:323px"></div>
</section>

<section class="contact">
  <div class="panel"></div>
  <h2 class="serif">Contact Us</h2>
  <div class="rule"></div>
  <div class="info" style="top:123px"><span class="ico"><svg width="18" height="22" viewBox="0 0 18 22"><path d="M9 0a8 8 0 0 0-8 8c0 6 8 14 8 14s8-8 8-14a8 8 0 0 0-8-8z" fill="#876aae"/><circle cx="9" cy="8" r="3" fill="#fff"/></svg></span><span>149 , Lorem Ipsum Dolor Sit Amet<br>United States</span></div>
  <div class="info" style="top:194px"><span class="ico"><svg width="20" height="14" viewBox="0 0 20 14"><rect width="20" height="14" rx="2" fill="#876aae"/><path d="M1 1l9 7 9-7" fill="none" stroke="#fff" stroke-width="1.5"/></svg></span><span>info@mirellesorvane.com</span></div>
  <div class="info" style="top:265px"><span class="ico"><svg width="18" height="18" viewBox="0 0 18 18"><path d="M4 1l3 4-2 2q2 4 6 6l2-2 4 3-2 3Q6 16 1 4z" fill="#876aae"/></svg></span><span>1 800 555 012</span></div>
  <div class="info" style="top:334px"><span class="ico"><svg width="18" height="20" viewBox="0 0 18 20"><rect x="1" y="4" width="16" height="15" rx="2" fill="#876aae"/><rect x="5" y="1" width="8" height="5" fill="#876aae"/><rect x="4" y="9" width="10" height="7" fill="#fff"/></svg></span><span>1 800 555 034</span></div>
  <a class="btn teal">Book an Appointment <svg class="arrow" viewBox="0 0 14 14"><rect x="1" y="2" width="12" height="11" rx="1" fill="none" stroke="#fff" stroke-width="1.5"/><line x1="1" y1="5.5" x2="13" y2="5.5" stroke="#fff" stroke-width="1.5"/></svg></a>
  <div class="map" role="img" aria-label="Street map showing the salon location"></div>
</section>

<footer class="site-footer">
  <div class="brand"><div class="mark">Maison Velour</div><div class="by">by MirelleSorvane</div></div>
  <nav class="footer-nav"><span>HOME</span><span>ABOUT US</span><span>OUR SERVICES</span><span>SHOPPING</span><span>GALLERY</span><span>CONTACT US</span></nav>
  <small>© 2021 Mirelle Sorvane.All Rights Reserved</small>
</footer>

</body>
</html>
```